Broschüre für Abdichtungen zu Bauwerken
Zielgruppe
Das Unternehmen Konrad Wiesholt produziert und vertreibt seit über 25 Jahren die einzigartigen KALVITEX®-Fertigmischungen zur Abdichtung von Gewässern, Bauwerken, Rohrleitungen, Deichen und Pflaster.
Wir möchten unsere Infromationsbroschüre neu gestalten lassen, eine rudimentär gestaltete Broschüre, die derzeit in Verwendung ist, liegt in Form einer PowerPoint-Datei bzw. PDF vor.
Aufgabenstellung
Klares und übersichtliches Layout, insbesondere gute Darstellung der vielen Auszüge aus Gutachten.
Benötigt wird eine InDesign-Datei/Template für die neuen Broschüren.

```html
<!DOCTYPE html>
<html lang="de">
<head>
<meta charset="utf-8">
<title>KALVITEX Broschüre</title>
<link href="https://fonts.googleapis.com/css2?family=Titillium+Web:wght@200;300;400;600;700&display=swap" rel="stylesheet">
<style>
:root{
  --green:#3d9e3a;
  --green-dark:#2f8a2d;
  --blue:#2fa3d5;
  --text:#707070;
  --text-dark:#555;
  --page:#fbfbfb;
  --bg:#dcdcdc;
}
*{margin:0;padding:0;box-sizing:border-box}
html,body{width:782px;height:1200px;overflow:hidden;background:var(--bg);font-family:"Titillium Web",sans-serif;color:var(--text)}
.canvas{position:relative;width:782px;height:1200px}
.spread{position:absolute;width:360px;height:254px;display:flex;box-shadow:0 2px 6px rgba(0,0,0,.12)}
.cover{position:absolute;width:180px;height:254px;background:var(--page);box-shadow:0 2px 6px rgba(0,0,0,.12)}
.page{position:relative;width:180px;height:254px;background:var(--page);overflow:hidden}
.page + .page{border-left:1px solid #e6e6e6}
.logo{position:absolute;top:12px;left:14px;font-weight:700;font-size:8px;letter-spacing:-.2px;color:var(--green)}
.url{position:absolute;bottom:10px;font-size:3.5px;font-weight:600;color:var(--blue)}
.folio{position:absolute;bottom:10px;font-size:3.5px;color:var(--blue)}
.title{font-weight:600;font-size:6.5px;color:var(--green);line-height:1.2}
.subtitle{font-weight:300;font-size:5.5px;color:var(--green);line-height:1.25}
.lead{font-weight:300;font-size:6px;color:var(--green);line-height:1.25}
.body{font-size:3.3px;line-height:1.45;color:var(--text)}
.abs{position:absolute}
.photo{position:absolute}
.photo-park{background:linear-gradient(180deg,#b9cbd6 0%,#6f8f4c 35%,#4d6e3c 60%,#7c9aa0 78%,#7a5b44 100%)}
.photo-tree{background:linear-gradient(180deg,#a8bccc 0%,#5e7f3c 30%,#456a32 60%,#5f7d6b 100%)}
.photo-leaves{background:linear-gradient(160deg,#9fc870 0%,#5f8f3e 45%,#cfe0b2 100%)}
.photo-digger{background:linear-gradient(180deg,#7ea3b8 0%,#5d7a3e 40%,#c99a4a 70%,#a07448 100%)}
.photo-basalt{background:linear-gradient(135deg,#5c6670 0%,#7e8790 50%,#4e5860 100%)}
.diagram{position:absolute;background:linear-gradient(180deg,#f4f4f4 0%,#7ec9e3 45%,#c99660 80%,#f4f4f4 100%)}
.cover-band{position:absolute;left:-10px;top:122px;width:124px;background:var(--green);color:#fff;padding:6px 8px}
.cover-band h1{font-size:5.6px;font-weight:600;line-height:1.25}
.cover-band p{font-size:5.2px;font-weight:300;line-height:1.3}
.cover-band small{display:block;font-size:2.8px;font-weight:600;letter-spacing:.2px;margin-top:3px}
.no-plastic{position:absolute;left:72px;top:159px;background:var(--blue);color:#fff;font-size:5px;font-weight:600;padding:0 2px}
.toc-row{display:flex;font-size:3.2px;color:var(--text);margin-bottom:4px}
.toc-row .dots{flex:1;border-bottom:.5px dotted #aaa;margin:0 2px 1px}
.blue-fill{position:absolute;background:var(--blue)}
.vorteile-word{position:absolute;left:16px;bottom:22px;writing-mode:vertical-rl;transform:rotate(180deg);font-size:44px;font-weight:200;line-height:1;color:#fff;white-space:nowrap}
.feature{position:absolute;color:#fff}
.feature h3{font-size:4.6px;font-weight:300;line-height:1.2;margin:3px 0 2px}
.feature p{font-size:2.7px;line-height:1.45;opacity:.9}
.feature svg{width:10px;height:10px}
.green-box{position:absolute;background:var(--green);color:#fff;padding:6px}
.green-box .body{color:#fff}
.side-note{position:absolute;font-size:2.8px;font-weight:600;color:var(--green);line-height:1.4}
.praxistipp{position:absolute;border:.5px solid var(--blue);padding:2px 3px;font-size:2.6px;color:var(--blue);background:#fff}
.praxistipp b{display:inline-block;background:var(--blue);color:#fff;font-size:2.8px;padding:0 2px;margin-bottom:1px}
.steps{position:absolute;list-style:none}
.steps li{display:flex;gap:3px;font-size:2.7px;line-height:1.35;margin-bottom:5px}
.steps li span{flex:none;width:5px;height:5px;border-radius:50%;background:var(--blue);color:#fff;font-size:2.8px;text-align:center;line-height:5px}
.ref{position:absolute;left:18px;width:140px;border-top:.5px solid var(--green);padding-top:4px}
.ref .meta{font-size:2.6px;font-weight:600;color:var(--text-dark)}
.ref .ref-title{font-size:4.2px;font-style:italic;font-weight:300;color:var(--text-dark);margin:2px 0}
.ref .quote{font-size:2.6px;font-style:italic;line-height:1.4}
.ref .sign{font-size:2.5px;font-weight:600;margin-top:3px}
.bullets{position:absolute;list-style:none;font-size:2.6px;line-height:1.4}
.bullets li{margin-bottom:2px}
</style>
</head>
<body>
<div class="canvas">

  <!-- Cover -->
  <div class="cover" style="left:100px;top:30px">
    <div class="logo">KALVITEX®</div>
    <div class="abs" style="top:14px;right:14px;font-size:3px">2022</div>
    <div class="photo photo-park" style="left:14px;top:28px;width:152px;height:188px" role="img" aria-label="Parkanlage mit Teich, Bäumen und Natursteinufer"></div>
    <div class="cover-band">
      <h1>Fertigmischungen zur Abdichtung</h1>
      <p>von Gewässern, Bauwerken, Rohrleitungen, Deichen und Pflaster.</p>
      <small>BEWÄHRTE QUALITÄT – SEIT ÜBER 25 JAHREN.</small>
    </div>
    <div class="no-plastic">NO PLASTIC</div>
    <div class="url" style="left:14px">www.kalvitex.de</div>
  </div>

  <!-- Spread: Inhaltsverzeichnis -->
  <div class="spread" style="left:402px;top:30px">
    <div class="page">
      <div class="logo">KALVITEX®</div>
      <div class="photo photo-tree" style="left:14px;top:28px;width:150px;height:200px" role="img" aria-label="Großer Baum an einem Teich mit Geländer"></div>
    </div>
    <div class="page">
      <div class="title abs" style="left:16px;top:24px;font-weight:400">Inhaltsverzeichnis</div>
      <div class="abs" style="left:16px;top:48px;width:150px">
        <div class="toc-row">Materialbeschreibung</div>
        <div class="toc-row">Was sind KALVITEX®-Fertigmischungen?<span class="dots"></span>04</div>
        <div class="toc-row">Vorteile gegenüber anderen Abdichtungen<span class="dots"></span>04</div>
        <div class="toc-row">Einsatzbereiche<span class="dots"></span>06</div>
        <div class="toc-row">A. Gewässer und Teichanlagen<span class="dots"></span>07</div>
        <div class="toc-row">B. Bauwerke und Rohrleitungen<span class="dots"></span>08</div>
        <div class="toc-row">C. Pflaster und Fugen<span class="dots"></span>09</div>
        <div class="toc-row">Anwendungsbeispiele und Referenzen<span class="dots"></span>10 – 14</div>
        <div class="toc-row">Materiallieferung, Lagerung und Langzeitlagerung<span class="dots"></span>15</div>
      </div>
      <div class="abs" style="left:16px;bottom:22px;font-size:3px">Stand: Januar 2022</div>
      <div class="url" style="left:16px">www.kalvitex.de</div>
    </div>
  </div>

  <!-- Spread: Vorteile -->
  <div class="spread" style="left:20px;top:320px">
    <div class="page">
      <div class="logo">KALVITEX®</div>
      <div class="blue-fill" style="left:10px;top:28px;width:170px;height:214px"></div>
      <div class="vorteile-word">Vorteile</div>
      <div class="feature" style="left:84px;top:40px;width:70px">
        <svg viewBox="0 0 20 20"><circle cx="10" cy="10" r="7" fill="none" stroke="#fff" stroke-width="1"/><path d="M10 3l2 2-2 2" fill="none" stroke="#fff" stroke-width="1"/></svg>
        <h3>Haltbar</h3>
        <p>Kein Schrumpfen und kein Austrocknen bei richtiger Anwendung. Die Mischung bleibt dauerhaft elastisch und dicht, auch bei starken Temperaturschwankungen.</p>
      </div>
      <div class="feature" style="left:84px;top:130px;width:70px">
        <svg viewBox="0 0 20 20"><path d="M4 13l4-8 4 8z M10 15h6" fill="none" stroke="#fff" stroke-width="1"/></svg>
        <h3>Recycelbar</h3>
        <p>Die Fertigmischung ist zu 100 % natürlich und frei von Kunststoffen. Sie kann nach Nutzung wieder ausgebaut und dem Boden zurückgegeben werden.</p>
      </div>
    </div>
    <div class="page">
      <div class="blue-fill" style="left:0;top:28px;width:168px;height:214px"></div>
      <div class="feature" style="left:12px;top:42px;width:68px">
        <svg viewBox="0 0 20 20"><circle cx="10" cy="8" r="4" fill="none" stroke="#fff" stroke-width="1"/><path d="M3 16c4-2 10-2 14 0" fill="none" stroke="#fff" stroke-width="1"/></svg>
        <h3>Kostengünstig und flexibel</h3>
        <p>Die Verarbeitung erfordert keine Spezialwerkzeuge. Das Material wird direkt auf der Baustelle eingebaut und passt sich jeder Form an.</p>
      </div>
      <div class="feature" style="left:88px;top:42px;width:68px">
        <svg viewBox="0 0 20 20"><rect x="3" y="4" width="14" height="12" fill="none" stroke="#fff" stroke-width="1"/><path d="M3 8h14M7 2v4M13 2v4" stroke="#fff" stroke-width="1"/></svg>
        <h3>Fast ganzjährig zu verarbeiten</h3>
        <p>Die Fertigmischung kann bei nahezu jeder Witterung eingebaut werden. Nur bei Frost muss die Verarbeitung ruhen.</p>
      </div>
      <div class="feature" style="left:12px;top:120px;width:68px">
        <svg viewBox="0 0 20 20"><path d="M10 18V9M10 9c-4 0-5-4-5-6 3 0 5 2 5 6zm0 0c4 0 5-4 5-6-3 0-5 2-5 6z" fill="none" stroke="#fff" stroke-width="1"/></svg>
        <h3>Begrünung mit speziellen Pflanzen zur Stabilisierung möglich</h3>
        <p>Die Oberfläche kann mit geeigneten Pflanzen begrünt werden. Das Wurzelwerk festigt die Schutzschicht und schont die Dichtung.</p>
      </div>
      <div class="url" style="left:12px;bottom:16px;color:#fff">www.kalvitex.de</div>
    </div>
  </div>

  <!-- Spread: Einbauhinweise -->
  <div class="spread" style="left:402px;top:320px">
    <div class="page">
      <div class="logo">KALVITEX®</div>
      <div class="title abs" style="left:30px;top:44px">Einbauhinweise</div>
      <div class="subtitle abs" style="left:30px;top:54px">Einbau allgemein</div>
      <p class="body abs" style="left:30px;top:64px;width:134px">Auf den vorbereiteten Untergrund wird die KALVITEX®-Fertigmischung lagenweise aufgebracht und verdichtet. Die Schichtstärke richtet sich nach der späteren Belastung. Nach dem Einbau ist die Oberfläche sofort abzudecken, damit sie nicht austrocknet. Bei größeren Flächen empfehlen wir eine Einweisung durch unsere Fachberater vor Ort.</p>
      <div class="subtitle abs" style="left:30px;top:118px">Einbau der Schutzschicht</div>
      <p class="body abs" style="left:30px;top:128px;width:134px">Um die Dichtung dauerhaft vor Austrocknung und Beschädigung zu schützen, wird direkt nach dem Einbau eine Schutzschicht aus Sand oder Kies aufgetragen. Die Stärke sollte mindestens 20 cm betragen. Ein Befahren der Fläche ist erst nach dem Aufbringen der Schutzschicht zulässig.</p>
      <div class="side-note" style="left:8px;top:160px;width:20px">Bei Unklarheiten empfehlen wir eine Beratung</div>
      <div class="folio" style="left:14px">8</div>
    </div>
    <div class="page">
      <div class="green-box" style="left:16px;top:38px;width:90px;height:70px">
        <p class="body" style="font-size:3px"><b>Anmerkung:</b><br>Vor der ersten Verarbeitung sollten die Angaben zum Untergrund geprüft werden. Die Empfehlungen dieser Broschüre ersetzen keine fachliche Planung. Für die Eignung im Einzelfall beraten wir Sie gern persönlich und erstellen auf Wunsch ein passendes Angebot für Ihr Bauvorhaben.</p>
      </div>
      <div class="subtitle abs" style="left:16px;top:140px">Bepflanzung</div>
      <p class="body abs" style="left:16px;top:150px;width:130px">Die Fläche kann mit flach wurzelnden Gräsern bepflanzt werden. Tief wurzelnde Gehölze sind zu vermeiden, da sie die Dichtung durchdringen können.</p>
      <div class="url" style="left:16px">www.kalvitex.de</div>
      <div class="folio" style="right:14px">9</div>
    </div>
  </div>

  <!-- Spread: Vorbereitung des Untergrunds -->
  <div class="spread" style="left:20px;top:610px">
    <div class="page">
      <div class="logo">KALVITEX®</div>
      <div class="title abs" style="left:30px;top:48px">Vorbereitung des Untergrunds</div>
      <p class="lead abs" style="left:30px;top:58px;width:138px">Nach dem Aushub ist das so hergestellte Planum zu verdichten, um ein ausreichend tragfestes Auflager für den Aufbau mit KALVITEX®-Fertigmischung zu gewährleisten. Weiterhin ist sicherzustellen, dass unter dem Planum keine Böden mit geringerer Festigkeit (z. B. organische Böden oder weiche bzw. locker gelagerte Böden) anstehen.</p>
      <div class="photo photo-digger" style="left:14px;top:128px;width:94px;height:68px" role="img" aria-label="Bagger beim Aushub auf einer Baustelle"></div>
      <div class="praxistipp" style="left:18px;top:192px;width:60px"><b>PRAXISTIPP</b><br>Ein Vlies unter der Dichtung schützt vor spitzen Steinen.</div>
      <p class="body abs" style="left:112px;top:128px;width:56px;font-size:2.7px">Der Untergrund muss frei von Wurzeln, Steinen und scharfkantigen Bestandteilen sein. Vor dem Einbau ist die Fläche glatt abzuziehen und gegebenenfalls mit Sand auszugleichen, damit die Dichtung gleichmäßig aufliegt.</p>
      <div class="folio" style="left:14px">10</div>
    </div>
    <div class="page">
      <div class="subtitle abs" style="left:16px;top:44px">Aufbau für Amphibienlaichgewässer</div>
      <p class="body abs" style="left:16px;top:54px;width:148px;font-size:2.8px">Das Gewässer sollte flach auslaufend angelegt werden. An den Seiten des Teiches wird die Dichtung bis über den höchsten Wasserstand geführt und mit einer Schutzschicht aus Sand abgedeckt.</p>
      <div class="diagram" style="left:24px;top:74px;width:130px;height:56px" role="img" aria-label="Schnittzeichnung: Gewässeraufbau mit Dichtung, Schutzschicht und Wasserspiegel"></div>
      <p class="body abs" style="left:20px;top:134px;width:140px;font-size:2.7px;font-weight:600;color:var(--text-dark)">Durch lang anhaltende Hitzeperioden und ausbleibenden Niederschlag liegt der Wasserspiegel unter der sichtbaren Schutzschicht.</p>
      <div class="diagram" style="left:24px;top:150px;width:130px;height:56px" role="img" aria-label="Schnittzeichnung: abgesunkener Wasserspiegel unter der Schutzschicht"></div>
      <div class="url" style="left:16px">www.kalvitex.de</div>
      <div class="folio" style="right:14px">11</div>
    </div>
  </div>

  <!-- Spread: Eignungsprüfung / Reparatur -->
  <div class="spread" style="left:402px;top:610px">
    <div class="page">
      <div class="logo">KALVITEX®</div>
      <div class="green-box" style="left:20px;top:30px;width:148px;height:136px">
        <p class="body" style="font-size:2.8px;font-weight:600">Eignungsprüfung (Auszug)</p>
        <p class="abs" style="left:6px;top:14px;width:130px;font-size:4.4px;font-style:italic;font-weight:300;line-height:1.25">„Eignungsprüfung des Fugenabdichtungsmaterials KALVITEX® Fertigmischung F“</p>
        <p class="body abs" style="left:6px;top:30px;width:134px;font-style:italic;font-size:2.8px">[…] Die Oberflächenbefestigung mit Pflaster ist in einem Teilbereich angehoben. Ursache ist eindringendes Wasser in die Fugen. Zur Abdichtung wurde das Material im Labor auf seine Eignung untersucht. Die Ergebnisse zeigen eine sehr geringe Durchlässigkeit und eine hohe Beständigkeit gegenüber Frost und Tausalz. […] Das Material ist für die vorgesehene Anwendung als Fugenabdichtung gut geeignet und kann ohne Einschränkung empfohlen werden. […]</p>
        <p class="body abs" style="left:6px;top:104px;width:130px;font-size:2.6px;font-weight:600">DIPL.-ING. M. R. FELLNER<br>Beratung – Planung – Prüflabor Erdbau<br>September 2019</p>
      </div>
      <div class="folio" style="left:14px">12</div>
    </div>
    <div class="page">
      <div class="title abs" style="left:14px;top:24px">Reparatur bei aufschwimmendem Pflaster</div>
      <div class="subtitle abs" style="left:14px;top:34px;width:130px">Maßnahmen im Bereich der Linden- und Mühlbachstrasse</div>
      <p class="abs" style="left:14px;top:52px;font-size:2.5px;letter-spacing:.2px">AUSZUG AUS DEM SANIERUNGSBERICHT</p>
      <p class="body abs" style="left:14px;top:60px;width:70px;font-size:2.7px">Im Kreuzungsbereich wurde ein Anheben der Pflastersteine festgestellt. Ursache war Wasser, das durch undichte Fugen in das Bettungsmaterial eindrang und bei Frost zu Hebungen führte. Nach dem Aufnehmen der Steine wurde das Bett erneuert und die Fugen mit KALVITEX®-Fertigmischung verfüllt. Seitdem ist die Fläche dauerhaft stabil und trocken.</p>
      <div class="abs" style="left:90px;top:60px;width:76px;font-size:2.8px;color:var(--blue)">Das Sanierungsverfahren besteht aus folgenden Arbeitsschritten:</div>
      <ul class="bullets" style="left:90px;top:70px;width:76px">
        <li>– Vorhandenes Pflaster aufnehmen und säubern</li>
        <li>– Bettung entfernen und Planum prüfen</li>
        <li>– Tragschicht neu einbauen und verdichten</li>
        <li>– Pflaster in frisches Bett verlegen</li>
        <li>– Fugen mit Fertigmischung F verfüllen</li>
        <li>– Oberfläche abkehren und einschlämmen</li>
      </ul>
      <div class="url" style="left:14px">www.kalvitex.de</div>
      <div class="folio" style="right:14px">13</div>
    </div>
  </div>

  <!-- Spread: Was sind Fertigmischungen -->
  <div class="spread" style="left:402px;top:900px">
    <div class="page">
      <div class="logo">KALVITEX®</div>
      <div class="photo photo-leaves" style="left:18px;top:30px;width:150px;height:196px" role="img" aria-label="Grüne Blätter an Zweigen vor hellem Hintergrund"></div>
    </div>
    <div class="page">
      <div class="title abs" style="left:14px;top:24px">Was sind KALVITEX®-Fertigmischungen?</div>
      <p class="lead abs" style="left:14px;top:34px;width:146px">KALVITEX®-Fertigmischungen sind von uns aus der eigenen langjährigen Praxis heraus entwickelte Tonmischungen, die in speziellen Produktionsanlagen hergestellt werden.</p>
      <p class="body abs" style="left:14px;top:66px;width:146px;font-size:2.8px">Bereits seit über 25 Jahren werden die Fertigmischungen als Abdichtungsmaterial erfolgreich eingesetzt. Sie bestehen aus natürlichen Rohstoffen und zeichnen sich durch folgende Eigenschaften aus:</p>
      <ol class="steps" style="left:14px;top:84px;width:70px">
        <li><span>1</span>Selbstheilende Wirkung bei Rissbildung</li>
        <li><span>2</span>Sie werden nach Rezeptur gemischt</li>
        <li><span>3</span>Gleichmäßige Verteilung der Bestandteile</li>
        <li><span>4</span>Hohe Dichtigkeit bei geringer Schichtstärke</li>
        <li><span>5</span>Leicht zu verarbeiten</li>
      </ol>
      <ol class="steps" style="left:90px;top:84px;width:70px">
        <li><span>6</span>Ständige Kontrolle im eigenen Labor</li>
        <li><span>7</span>Frei von Kunststoffen und Zusätzen</li>
        <li><span>8</span>Große Mengen kurzfristig lieferbar</li>
        <li><span>9</span>Bei richtiger Lagerung lange haltbar</li>
        <li><span>10</span>Auch nach Jahren wieder verwendbar</li>
      </ol>
      <div class="url" style="left:14px">www.kalvitex.de</div>
      <div class="folio" style="right:14px">5</div>
    </div>
  </div>

  <!-- Spread: Kolkschutz / Referenzen -->
  <div class="spread" style="left:20px;top:900px">
    <div class="page">
      <div class="logo">KALVITEX®</div>
      <div class="title abs" style="left:14px;top:30px">Kolkschutz bei Brückenfundament</div>
      <p class="lead abs" style="left:14px;top:40px;width:146px">Die KALVITEX®-Fertigmischung F zur Verfüllung von Fugen bei Basaltsäulenpflaster, hier am Beispiel der neuen Rheinbrücke in Wesel – ein Einsatzort der besonderen Art.</p>
      <div class="photo photo-basalt" style="left:14px;top:80px;width:106px;height:150px" role="img" aria-label="Bildraster: Basaltsäulenpflaster mit verfüllten Fugen"></div>
      <p class="body abs" style="left:124px;top:80px;width:44px;font-size:2.6px">Rund um die Pfeiler der Brücke wurde ein Kolkschutz aus Basaltsäulen verlegt. Die Fugen wurden mit der Fertigmischung F verfüllt, um ein Ausspülen durch die Strömung zu verhindern. Auch nach mehreren Hochwassern ist die Verfüllung intakt und die Fläche stabil.</p>
      <div class="folio" style="left:14px">14</div>
    </div>
    <div class="page">
      <div class="title abs" style="left:18px;top:28px">Auszug aus Referenzschreiben</div>
      <div class="ref" style="top:52px">
        <p class="meta">BV: Discountermarkt in Nordhausen</p>
        <p class="ref-title">Abdichtung der Park- und Fahrflächen mit KALVITEX®-Fertigmischung F</p>
        <p class="quote">„Durch den Einsatz der Fertigmischung konnte das Eindringen von Oberflächenwasser in die Pflasterbettung dauerhaft verhindert werden. Die Flächen sind seit dem Einbau ohne Schäden.“ […]</p>
        <p class="sign">DIPL.-GEOL. L. BRANDT, BRANDT &amp; PARTNER, JANUAR 2007</p>
      </div>
      <div class="ref" style="top:130px">
        <p class="meta">BV: Gartencenter und Gemüsebaubetrieb in Altfeld</p>
        <p class="ref-title">Abdichtung der Fahr- und Parkplatzbereiche mit KALVITEX®-Fertigmischung F</p>
        <p class="quote">„Die Verarbeitung war unkompliziert, und das Ergebnis überzeugt uns bis heute. Wir können das Material uneingeschränkt empfehlen.“ […]</p>
        <p class="sign">JONAS HARRER LANDSCHAFTSARCHITEKT, APRIL 2010</p>
      </div>
      <div class="url" style="left:18px">www.kalvitex.de</div>
      <div class="folio" style="right:14px">15</div>
    </div>
  </div>

</div>
</body>
</html>
```